Customer Dashboard Design for Email Security SaaS

Mailvarden is a commercial email spam filter offered as a SaaS product, built and operated by a small German hosting provider. It protects business email accounts against spam, phishing, scam, and viruses using a multilayer filtering pipeline that combines traditional spam detection with AI-powered classification. The product runs entirely on German infrastructure, ensuring data sovereignty for European customers.

We need a complete redesign of the customer-facing dashboard. This is the web application where paying customers manage their email filtering: view their mail log, check quarantined emails, manage allow/blocklists, configure their settings, and handle their subscription. It is the primary touchpoint between Mailvarden and its customers.

Our customers are system administrators, IT managers at small-to-medium businesses, and operators of small hosting providers. They are technically competent but not designers. They expect professional, efficient tools that respect their time. They typically manage 10–500 email accounts and check the dashboard a few times per week, with heavier use during spam incidents.

We have attached the current mockups which really need to be replaced with something good looking.

Target Market(s)

System administrators, IT managers at small-to-medium businesses, and operators of small hosting providers.

Industry/Entity Type

SaaS

Number of Pages Required

5+ page

```html
<!DOCTYPE html>
<html lang="de">
<head>
<meta charset="utf-8">
<title>Mailvarden – Einstellungen</title>
<link href="https://fonts.googleapis.com/css2?family=Poppins:wght@400;500;600&display=swap" rel="stylesheet">
<style>
:root{
  --sidebar:#55514a;
  --header:#55514a;
  --orange:#ee8228;
  --orange-soft:#fdf2e7;
  --page:#f3f3f4;
  --card:#ffffff;
  --text:#2a2824;
  --muted:#55514a;
  --line:#cfcfcf;
  --track:#f3ece3;
  --panel:#f3f3f4;
  --green:#3f8a52;
}
*{box-sizing:border-box;margin:0;padding:0}
html,body{width:1079px;height:1200px;overflow:hidden;background:var(--page)}
body{font-family:'Poppins',sans-serif;color:var(--text)}
.stage{position:absolute;left:0;top:0;width:1700px;height:1890px;transform:scale(0.63471);transform-origin:0 0;background:var(--page)}
.abs{position:absolute}
.sidebar{left:0;top:0;width:452px;height:1890px;background:var(--sidebar)}
.brand{left:40px;top:58px;display:flex;align-items:center;gap:24px}
.brand-mark{width:72px;height:72px;border-radius:18px;background:#7a766f}
.brand-name{color:#fff;font-size:40px;font-weight:500}
.nav{left:40px;top:180px;width:368px}
.nav-item{display:flex;align-items:center;gap:20px;height:64px;padding-left:20px;color:#fff;font-size:21px;margin-bottom:10px;border-radius:4px}
.nav-item svg{width:30px;height:30px;stroke:#fff;fill:none;stroke-width:1.6}
.nav-item.active{background:var(--orange)}
.search{left:580px;top:30px;width:358px;height:56px;background:#fff;border-radius:28px;padding:0 26px;display:flex;align-items:center;justify-content:space-between;font-size:17px;color:#555}
.user{left:958px;top:34px;display:flex;align-items:center;gap:16px;font-size:19px}
.avatar{width:46px;height:46px;border-radius:50%;background:var(--sidebar);display:flex;align-items:center;justify-content:center}
.btn-top{top:30px;height:56px;display:flex;align-items:center;justify-content:center;gap:10px;color:#fff;font-size:19px;font-weight:500;border-radius:3px}
.btn-top svg{stroke:#fff;fill:none;stroke-width:1.6}
.card{left:520px;top:150px;width:1148px;height:1682px;background:var(--card);border-radius:18px}
.hero{left:512px;top:126px;width:1148px;height:170px;background:var(--header);border-radius:18px}
.hero-icon{left:553px;top:161px;width:100px;height:100px;border-radius:50%;background:#fff;display:flex;align-items:center;justify-content:center}
.hero-title{left:674px;top:152px;color:#fff;font-size:64px;font-weight:600;line-height:1.2}
.hero-sub{left:674px;top:238px;color:#fff;font-size:21px}
h2{font-size:26px;font-weight:500;color:var(--text)}
.desc{font-size:18px;color:var(--muted);line-height:1.5}
.label{font-size:18px;color:var(--text);font-weight:500;letter-spacing:.2px}
.field{width:630px;height:60px;border:1px solid var(--line);border-radius:3px;display:flex;align-items:center;justify-content:space-between;padding:0 16px 0 20px;font-size:16px;letter-spacing:1px}
.btn{background:var(--orange);color:#fff;font-size:18px;font-weight:500;display:flex;align-items:center;justify-content:center;border-radius:3px}
.req{left:1230px;top:483px;width:400px;height:265px;background:var(--panel);border-radius:6px;padding:30px}
.req h3{font-size:20px;font-weight:500;margin-bottom:16px}
.req li{list-style:none;display:flex;align-items:center;gap:10px;font-size:18px;color:var(--muted);height:40px}
.slider-track{left:542px;top:1081px;width:780px;height:14px;border-radius:7px;background:var(--track)}
.slider-fill{left:542px;top:1081px;width:500px;height:14px;border-radius:7px;background:var(--orange)}
.slider-thumb{left:1030px;top:1076px;width:24px;height:24px;border-radius:50%;background:var(--orange);border:2px solid #fff}
.tick{top:1116px;font-size:18px;color:var(--muted)}
.num{height:60px;border:1px solid var(--line);border-radius:3px;display:flex;align-items:center;justify-content:space-between;padding:0 20px;font-size:18px;color:var(--muted)}
.opt{top:1491px;width:340px;height:216px;border:1px solid var(--line);border-radius:6px;padding:28px 26px 0 54px}
.opt.selected{background:var(--orange-soft);border-color:#f0c9a0}
.opt .radio{position:absolute;left:20px;top:30px;width:16px;height:16px;border-radius:50%;border:1px solid #bbb}
.opt.selected .radio{border:4px solid var(--orange);background:#fff}
.opt h4{font-size:20px;font-weight:500;margin:18px 0 12px}
.opt p{font-size:16px;color:var(--muted);line-height:1.5}
.opt svg{fill:none;stroke-width:1.6}
</style>
</head>
<body>
<div class="stage">
  <aside class="abs sidebar">
    <div class="abs brand"><div class="brand-mark"></div><span class="brand-name">Mailvarden</span></div>
    <nav class="abs nav">
      <div class="nav-item"><svg viewBox="0 0 30 30"><path d="M4 14 15 4l11 10M7 12v13h6v-7h4v7h6V12"/></svg>Übersicht</div>
      <div class="nav-item active"><svg viewBox="0 0 30 30"><rect x="3" y="7" width="24" height="16"/><path d="m3 7 12 9 12-9"/></svg>Mail-Log</div>
      <div class="nav-item"><svg viewBox="0 0 30 30"><rect x="3" y="7" width="24" height="16"/><path d="m3 7 12 9 12-9M3 23l9-8M27 23l-9-8"/></svg>Postfächer</div>
      <div class="nav-item"><svg viewBox="0 0 30 30"><path d="M15 3 5 7v8c0 6 4 10 10 12 6-2 10-6 10-12V7z"/><path d="m11 15 3 3 5-6"/></svg>Allowlist</div>
      <div class="nav-item"><svg viewBox="0 0 30 30"><path d="M15 4 3 26h24z"/><path d="M15 12v7M15 22v1"/></svg>Blocklist</div>
      <div class="nav-item"><svg viewBox="0 0 30 30"><circle cx="15" cy="15" r="4"/><path d="M15 3v4M15 23v4M3 15h4M23 15h4M6.5 6.5l3 3M20.5 20.5l3 3M6.5 23.5l3-3M20.5 9.5l3-3"/></svg>Einstellungen</div>
      <div class="nav-item"><svg viewBox="0 0 30 30"><path d="M7 3h16v24l-3-2-2 2-3-2-3 2-2-2-3 2z"/><path d="M11 10h8M11 15h8M11 20h5"/></svg>Abrechnung</div>
    </nav>
  </aside>

  <div class="abs search">Suchen<svg width="22" height="22" viewBox="0 0 22 22" fill="none" stroke="#555" stroke-width="1.6"><circle cx="9" cy="9" r="7"/><path d="m14 14 6 6"/></svg></div>
  <div class="abs user"><div class="avatar"><svg width="24" height="24" viewBox="0 0 24 24" fill="none" stroke="#fff" stroke-width="1.5"><circle cx="12" cy="8" r="4"/><path d="M4 22c0-5 4-8 8-8s8 3 8 8"/></svg></div>Willkommen zurück, Jonas!</div>
  <div class="abs btn-top" style="left:1275px;width:200px;background:var(--orange)"><svg width="22" height="26" viewBox="0 0 22 26"><rect x="2" y="11" width="18" height="13"/><path d="M6 11V7a5 5 0 0 1 10 0v4M11 16v4"/></svg>Quarantäne</div>
  <div class="abs btn-top" style="left:1485px;width:175px;background:var(--sidebar)"><svg width="32" height="22" viewBox="0 0 32 22"><rect x="2" y="2" width="26" height="18"/><path d="m2 2 13 10 13-10"/></svg>Mail Log</div>

  <div class="abs card"></div>
  <div class="abs hero"></div>
  <div class="abs hero-icon"><svg width="60" height="60" viewBox="0 0 30 30" fill="none" stroke="#b8aa98" stroke-width="1.6"><circle cx="15" cy="15" r="4"/><path d="M13 3h4l1 3 3 1.5 3-1.5 3 3-1.5 3L26 13v4l-3 1-1.5 3 1.5 3-3 3-3-1.5L15 27h-2l-1-3-3-1.5-3 1.5-3-3 1.5-3L4 17v-4l3-1 1.5-3L7 6l3-3 3 1.5z"/></svg></div>
  <div class="abs hero-title">Einstellungen</div>
  <div class="abs hero-sub">Verwalte deine Sicherheits- and Datenschutzoptionen</div>

  <h2 class="abs" style="left:542px;top:350px">Passwort andern</h2>
  <p class="abs desc" style="left:542px;top:390px">Aktualisiere dein Passwort, urn dein Konto zu sichern.</p>
  <div class="abs label" style="left:542px;top:447px">Aktuelles Passwort</div>
  <div class="abs field" style="left:542px;top:485px">••••••••••••••••••••••••••<svg width="28" height="18" viewBox="0 0 28 18" fill="none" stroke="#444" stroke-width="1.6"><path d="M2 9c4-7 20-7 24 0-4 7-20 7-24 0z"/><circle cx="14" cy="9" r="3.5"/></svg></div>
  <div class="abs label" style="left:542px;top:567px">Neues Passwort</div>
  <div class="abs field" style="left:542px;top:605px">••••••••••••••••••••••••••<svg width="28" height="18" viewBox="0 0 28 18" fill="none" stroke="#444" stroke-width="1.6"><path d="M2 9c4-7 20-7 24 0-4 7-20 7-24 0z"/><circle cx="14" cy="9" r="3.5"/></svg></div>
  <div class="abs label" style="left:542px;top:687px">Neues Passwort bestatigen</div>
  <div class="abs field" style="left:542px;top:725px">••••••••••••••••••••••••••<svg width="28" height="18" viewBox="0 0 28 18" fill="none" stroke="#444" stroke-width="1.6"><path d="M2 9c4-7 20-7 24 0-4 7-20 7-24 0z"/><circle cx="14" cy="9" r="3.5"/></svg></div>
  <div class="abs btn" style="left:542px;top:815px;width:200px;height:56px">Passwort Ändern</div>

  <div class="abs req">
    <h3>Passwortanforderungen:</h3>
    <ul>
      <li><svg width="22" height="22" viewBox="0 0 22 22" fill="none" stroke="#3f8a52" stroke-width="1.8"><circle cx="11" cy="11" r="9"/><path d="m6 11 4 4 8-9"/></svg>Mindestens 12 Zeichen</li>
      <li><svg width="22" height="22" viewBox="0 0 22 22" fill="none" stroke="#3f8a52" stroke-width="1.8"><circle cx="11" cy="11" r="9"/><path d="m6 11 4 4 8-9"/></svg>GroB- and Kleinbuchstaben</li>
      <li><svg width="22" height="22" viewBox="0 0 22 22" fill="none" stroke="#3f8a52" stroke-width="1.8"><circle cx="11" cy="11" r="9"/><path d="m6 11 4 4 8-9"/></svg>Mindestens eine Zahl</li>
      <li><svg width="22" height="22" viewBox="0 0 22 22" fill="none" stroke="#3f8a52" stroke-width="1.8"><circle cx="11" cy="11" r="9"/><path d="m6 11 4 4 8-9"/></svg>Mindestens ein Sonderzeichen</li>
    </ul>
  </div>

  <h2 class="abs" style="left:542px;top:918px">Aufbewahrungsfrist</h2>
  <p class="abs desc" style="left:542px;top:958px">Lege fest, wie lange markierte E-Mails im System aufbewahrt werden.</p>
  <div class="abs desc" style="left:542px;top:1035px;color:var(--text)">Aufbewahrungsdauer fiir markierte E-Mails</div>
  <div class="abs slider-track"></div>
  <div class="abs slider-fill"></div>
  <div class="abs slider-thumb"></div>
  <div class="abs tick" style="left:542px">30 Tag</div>
  <div class="abs tick" style="left:775px">90 Tag</div>
  <div class="abs tick" style="left:1007px">180 Tag</div>
  <div class="abs tick" style="left:1247px">365 Tag</div>
  <div class="abs num" style="left:1450px;top:1048px;width:180px"><span>180</span><span>Tag</span></div>

  <h2 class="abs" style="left:542px;top:1190px">Anonymisierungszeitraum</h2>
  <p class="abs desc" style="left:542px;top:1229px;width:460px">Lege fest, nach wie vielen Tagen Log-Eintrage anonymisiert werden.</p>
  <div class="abs desc" style="left:1078px;top:1195px;color:var(--text)">Anonymisierungszeitraum für Log-Einträge</div>
  <div class="abs num" style="left:1078px;top:1235px;width:180px"><span>180</span><span>Tag</span></div>
  <div class="abs" style="left:1078px;top:1316px;font-size:15px;color:var(--muted)">Lege fest, nach wie vielen Tagen Log-Eintrage anonymisiert werden.</div>

  <h2 class="abs" style="left:542px;top:1385px">Verhalten bei UbergroBen E-Mails</h2>
  <p class="abs desc" style="left:542px;top:1424px">Lege fest, wie mit E-Mails umgegangen werden soil, due maximale GthBenbegrenzung Uberschreiten.</p>

  <div class="abs opt selected" style="left:542px"><span class="radio"></span>
    <svg width="60" height="46" viewBox="0 0 60 46" stroke="#ee8228"><rect x="2" y="4" width="40" height="28"/><path d="m2 4 20 15 20-15"/><path d="M46 22l10 4v8c0 5-4 8-10 10-6-2-10-5-10-10v-8z" fill="#fdf2e7"/><circle cx="46" cy="33" r="4"/><path d="m43 36 6-6"/></svg>
    <h4>E-Mail ablehnen</h4><p>Die E-Mail wird abgelehnt und der Absender erhalt eine Fehlermeldung.</p></div>
  <div class="abs opt" style="left:912px"><span class="radio"></span>
    <svg width="60" height="46" viewBox="0 0 60 46" stroke="#9a9088"><rect x="2" y="10" width="40" height="28"/><path d="m2 10 20 15 20-15M2 38l15-12M42 38 27 26"/><circle cx="48" cy="10" r="8" fill="#fff"/><path d="m45 7 6 6M51 7l-6 6"/></svg>
    <h4>E-Mail zurdckweisen</h4><p>Die E-Mail wird zurOckgewiesen und der Absender kann es emeut versuchen.</p></div>
  <div class="abs opt" style="left:1282px"><span class="radio"></span>
    <svg width="60" height="46" viewBox="0 0 60 46" stroke="#9a9088"><rect x="2" y="2" width="40" height="30"/><path d="m2 2 20 15 20-15"/><circle cx="44" cy="34" r="9" fill="#fff"/><path d="m40 34 3 3 6-6"/></svg>
    <h4>E-Mail akzeptieren</h4><p>Die E-Mail wird akzeptiert, aber Anhange werden entfernt.</p></div>

  <div class="abs btn" style="left:542px;top:1737px;width:270px;height:56px">Einstellungen Speichern</div>
</div>
</body>
</html>
```